Alapca breeding needs a website

Presentation of the farm, animals (stallions, mares, information about the animals, for sale) and possible later expansion with a webshop (alpaca wool products). We want to present our farm and the animals on the farm on this page. A mission why we are doing this. Furthermore, each animal should be shown with a picture and described. Later we want to sell our own products made from alpaca wool via a webshop. But we still need to grow a bit to do that.

Target Market(s)

Information about my alpaca breeding and the alpaca farm

Industry/Entity Type

Tierzucht

Number of Pages Required

1 page

Font styles to use
Sans Serif

Requirements
Must have
• Modern design that matches the logo
Nice to have
• Intuitive operation / Clear structure
Should not have
• No

```html
<!DOCTYPE html>
<html lang="en">
<head>
<meta charset="utf-8">
<title>Lunara Alpacas — Alpaca Farm</title>
<link href="https://fonts.googleapis.com/css2?family=Roboto:wght@500;700;900&family=Inter:wght@400;500;600;700&display=swap" rel="stylesheet">
<style>
:root{
  --green:#8cc63f;
  --green-dark:#6ea82a;
  --navy:#0c2340;
  --cream:#fff5e8;
  --text:#222;
  --muted:#555;
  --white:#fff;
  --star:#f2b705;
}
*{box-sizing:border-box;margin:0;padding:0}
html,body{width:1200px;height:4953px;overflow:hidden}
body{position:relative;background:var(--white);font-family:"Inter",sans-serif;color:var(--text)}
.abs{position:absolute}
h1,h2,h3{font-family:"Roboto",sans-serif;font-weight:700;letter-spacing:.5px}
p{font-size:13px;line-height:22px}
.btn{position:absolute;display:flex;align-items:center;justify-content:center;background:var(--navy);color:var(--white);font-size:11px;font-weight:700;letter-spacing:.5px;clip-path:polygon(6% 0,100% 0,94% 100%,0 100%);height:40px;width:150px}
.btn.light{background:var(--white);color:var(--navy)}
.photo{position:absolute}

/* nav */
.nav{top:0;left:0;width:1200px;height:81px;background:var(--white)}
.brand{position:absolute;left:126px;top:30px;display:flex;align-items:center;gap:8px;font-family:"Roboto",sans-serif;font-weight:700;font-size:16px;color:var(--navy);letter-spacing:1px}
.brand .dot{width:14px;height:14px;border-radius:50%;background:var(--green)}
.menu{position:absolute;top:33px;left:466px;display:flex;gap:52px;font-size:13px;font-weight:500}
.menu .active{color:var(--green);position:relative}
.menu .active::after{content:"•••";position:absolute;left:8px;top:16px;font-size:10px;color:var(--navy);letter-spacing:1px}
.nav-icons{position:absolute;top:30px;left:1012px;display:flex;gap:14px;align-items:center}

/* hero */
.hero{top:81px;left:0;width:1200px;height:669px;background:linear-gradient(90deg,#141a0c 0%,#3d4a1c 35%,#8a8a2c 65%,#c4a43a 100%)}
.hero::after{content:"";position:absolute;left:0;bottom:0;width:100%;height:220px;background:linear-gradient(0deg,#6d8d1e,transparent)}
.hero h1{position:absolute;left:125px;top:190px;font-size:52px;line-height:58px;color:var(--white);z-index:1}
.hero p{position:absolute;left:125px;top:390px;width:490px;color:var(--white);font-size:12.5px;z-index:1}

/* about */
.cream-box{position:absolute;background:var(--cream)}
.sec-title{font-size:34px;color:var(--text)}
.seal{position:absolute;left:721px;top:877px;width:104px;height:104px;border-radius:50%;background:var(--green);border:4px solid #b9e07f;display:flex;align-items:center;justify-content:center;color:var(--white);font-family:"Roboto",sans-serif;font-weight:700;font-size:12px;letter-spacing:1px;z-index:2}
.round-arrow{position:absolute;left:277px;top:1779px;width:58px;height:58px;border-radius:50%;background:var(--green);border:4px solid #c9eb9a;z-index:2}

/* achievement */
.achieve{top:1990px;left:0;width:1200px;height:506px;background:linear-gradient(90deg,#3b2a1c,#5b4330 50%,#3a2a1e)}
.achieve h2{position:absolute;right:125px;top:96px;font-size:36px;color:var(--white)}
.achieve p{position:absolute;right:125px;top:150px;width:540px;text-align:right;color:var(--white);font-size:12.5px}
.stat{position:absolute;top:264px;width:154px;height:140px;background:var(--white);text-align:center;padding-top:22px}
.stat b{display:block;font-family:"Roboto",sans-serif;font-size:24px;margin-top:10px}
.stat b sup{color:var(--green);font-size:12px}
.stat span{font-size:13px;color:var(--text)}

/* products */
.prod-green{top:2496px;left:673px;width:527px;height:931px;background:var(--green)}
.eyebrow{font-size:11px;font-weight:700;letter-spacing:2px;color:var(--green);display:flex;align-items:center;gap:8px}
.eyebrow::after{content:"";width:44px;height:2px;background:var(--green)}
.card{position:absolute;background:var(--white);padding:12px;box-shadow:0 4px 18px rgba(0,0,0,.08)}
.card .img{width:100%;height:196px}
.card h4{font-size:12px;letter-spacing:2px;color:var(--green);margin:30px 18px 8px;font-weight:700}
.card p{font-size:10px;line-height:16px;color:var(--muted);margin:0 18px}
.stars{color:var(--star);font-size:10px;letter-spacing:2px;margin:6px 18px}

/* animals */
.animals{top:3427px;left:0;width:1200px;height:750px;background:var(--navy)}
.animals .eyebrow{position:absolute;left:0;width:1200px;justify-content:center;top:100px}
.animals .eyebrow::before{content:"";width:44px;height:2px;background:var(--green)}
.animals h2{position:absolute;left:0;width:1200px;text-align:center;top:132px;font-size:36px;color:var(--white);font-weight:500}
.acard{position:absolute;top:223px;width:221px;height:350px;background:var(--white);padding:12px}
.acard .img{height:200px}
.acard h4{font-size:12px;letter-spacing:2px;color:var(--green);margin:22px 0 8px;font-weight:700}
.acard h4 small{font-size:8px;color:var(--text);letter-spacing:0;font-weight:500;margin-left:6px}
.acard p{font-size:10px;line-height:15px;color:var(--muted)}
.acard .stars{margin:6px 0}
.acard .price{font-weight:700;color:var(--green);font-size:16px}
.chev{position:absolute;width:30px;height:30px;border-radius:50%;background:var(--green);display:flex;align-items:center;justify-content:center;z-index:3}
.chev.white{background:var(--white)}

/* footer */
.footer{top:4510px;left:0;width:1200px;height:375px;background:var(--green)}
.f-brand{position:absolute;left:128px;top:176px;font-family:"Roboto",sans-serif;font-weight:700;font-size:20px;color:var(--white);letter-spacing:1px;display:flex;align-items:center;gap:8px}
.f-brand .dot{width:16px;height:16px;border-radius:50%;background:var(--white)}
.socials{position:absolute;left:125px;top:236px;display:flex;gap:14px}
.socials span{width:28px;height:28px;border-radius:50%;border:2px solid var(--navy)}
.links{position:absolute;left:340px;top:104px;color:var(--white);font-size:12px}
.links h5{font-size:12px;font-weight:700;letter-spacing:1px;margin-bottom:18px}
.links li{list-style:none;margin-bottom:17px}
.tile-panel{position:absolute;left:546px;top:4446px;width:529px;height:385px;background:var(--green)}
.copy{position:absolute;top:4885px;left:0;width:1200px;height:68px;display:flex;align-items:center;justify-content:center;font-size:12px}
.tile{position:absolute;width:166px;height:166px}
</style>
</head>
<body>

<header class="abs nav">
  <div class="brand"><span class="dot"></span>LUNARA ALPACAS</div>
  <nav class="menu">
    <span class="active">Home</span><span>About Us</span><span>Animals</span><span>Shop</span><span>Inquire Now</span>
  </nav>
  <div class="nav-icons">
    <svg width="18" height="16" viewBox="0 0 18 16" fill="none" stroke="#8cc63f" stroke-width="1.8"><path d="M1 2h3l2 9h9l2-7H5"/><circle cx="7" cy="14" r="1.3"/><circle cx="14" cy="14" r="1.3"/></svg>
    <span style="width:1px;height:14px;background:#ccc"></span>
    <svg width="16" height="16" viewBox="0 0 16 16" fill="none" stroke="#8cc63f" stroke-width="1.8"><circle cx="7" cy="7" r="5"/><path d="M11 11l4 4"/></svg>
  </div>
</header>

<section class="abs hero" role="img" aria-label="Sunlit pasture with grazing alpacas and a windmill at the edge of the field">
  <h1>INDULGE IN<br>THE SOFTNESS<br>OF ALPACA WOOL</h1>
  <p>Lorem Ipsum is simply dummy text of the printing and typesetting industry. Lorem Ipsum has been the industry's standard dummy text ever since the 1500s, when an unknown printer took a galley of type and scrambled it to make a type specimen book.</p>
</section>

<!-- About -->
<div class="photo" style="left:0;top:885px;width:346px;height:548px;background:linear-gradient(160deg,#9a8f7a,#6b5a3a 55%,#5e6b34)" role="img" aria-label="Child riding a chestnut horse led by an adult beside a fence"></div>
<div class="cream-box" style="left:346px;top:929px;width:448px;height:373px"></div>
<div class="photo" style="left:794px;top:850px;width:406px;height:383px;background:linear-gradient(170deg,#6f8a8f,#7a8f4c 40%,#6b7f3a)" role="img" aria-label="Woman feeding two woolly alpacas in a green field"></div>
<div class="seal">LUNARA</div>
<h2 class="abs sec-title" style="left:402px;top:980px">ABOUT US</h2>
<p class="abs" style="left:402px;top:1032px;width:340px">Lorem Ipsum is simply dummy text of the printing and typesetting industry. Lorem Ipsum has been the industry's standard dummy text ever since the 1500s, when an unknown printer took a galley of type and scrambled it to make a type specimen book.</p>
<div class="btn" style="left:404px;top:1201px">READ MORE</div>

<!-- Story -->
<div class="photo" style="left:21px;top:1385px;width:567px;height:423px;background:linear-gradient(120deg,#4b4f4a,#b9b4a6 50%,#6d6c62)" role="img" aria-label="White alpaca standing in front of a pen fence"></div>
<div class="round-arrow"><svg width="50" height="50" viewBox="0 0 50 50" fill="none" stroke="#fff" stroke-width="2"><path d="M16 25h18M28 19l6 6-6 6"/></svg></div>
<div class="cream-box" style="left:640px;top:1404px;width:435px;height:484px"></div>
<h2 class="abs sec-title" style="left:640px;width:435px;text-align:center;top:1452px">OUR STORY</h2>
<p class="abs" style="left:676px;top:1505px;width:363px;text-align:center">Lorem Ipsum is simply dummy text of the printing and typesetting industry. Lorem Ipsum has been the industry's standard dummy text ever since the 1500s, when an unknown printer took a galley of type and scrambled it to make a type specimen book. It has survived not only five centuries, but also the leap into electronic typesetting, remaining essentially unchanged. It was popularised in the 1960s with the release of Letraset sheets containing Lorem Ipsum passages, and more recently with desktop publishing software like Aldus PageMaker including versions.</p>
<div class="btn" style="left:780px;top:1792px">THE ANIMALS</div>

<!-- Achievement -->
<section class="abs achieve" role="img" aria-label="Woman sitting with alpacas in a wooden barn">
  <h2>THE ACHIEVMENT</h2>
  <p>Lorem Ipsum is simply dummy text of the printing and typesetting industry. Lorem Ipsum has been the industry's standard dummy text ever since the 1500s, when an unknown printer took a galley of type and scrambled it to make a type specimen book.</p>
  <div class="stat" style="left:573px"><svg width="34" height="30" viewBox="0 0 34 30" fill="none" stroke="#8cc63f" stroke-width="1.6"><path d="M3 14l7-6 6 4 6-4 9 6-12 10z"/></svg><b>150<sup>+</sup></b><span>Finished Projects</span></div>
  <div class="stat" style="left:748px"><svg width="34" height="30" viewBox="0 0 34 30" fill="none" stroke="#8cc63f" stroke-width="1.6"><circle cx="17" cy="8" r="4"/><circle cx="7" cy="12" r="3"/><circle cx="27" cy="12" r="3"/><path d="M10 26c0-6 14-6 14 0M2 26c0-4 6-5 8-3M32 26c0-4-6-5-8-3"/></svg><b>100<sup>+</sup></b><span>Professional Team</span></div>
  <div class="stat" style="left:921px"><svg width="34" height="30" viewBox="0 0 34 30" fill="none" stroke="#8cc63f" stroke-width="1.6"><circle cx="17" cy="8" r="4"/><path d="M5 20h8l6 3 10-6M5 26h24"/></svg><b>120<sup>+</sup></b><span>Happy Customer</span></div>
</section>
<div class="photo" style="left:0;top:1894px;width:400px;height:602px;background:linear-gradient(180deg,#8a5a34 0%,#6a4628 60%,#4f8a2e 100%)" role="img" aria-label="Chestnut horse standing on green grass"></div>

<!-- Products -->
<div class="abs prod-green"></div>
<div class="abs eyebrow" style="left:125px;top:2682px">OUR PRODUCT</div>
<h2 class="abs" style="left:125px;top:2704px;font-size:36px;line-height:47px">WOOL THAT WARMS<br>YOUR HEART AND<br>HOME</h2>
<p class="abs" style="left:125px;top:2870px;width:370px">Lorem Ipsum is simply dummy text of the printing and typesetting industry. Lorem Ipsum has been the industry's standard dummy text ever since the 1500s, when an unknown printer took a galley of type and scrambled it to make a type specimen book.</p>
<p class="abs" style="left:125px;top:2998px;width:370px">Lorem Ipsum is simply dummy text of the printing and typesetting industry. Lorem Ipsum has been the industry's standard dummy text ever since the 1500s, when an unknown printer took a galley of type and scrambled it to make a type specimen book.</p>
<div class="btn" style="left:129px;top:3145px">SHOP NOW</div>

<div class="card" style="left:546px;top:2565px;width:254px;height:377px"><div class="img" role="img" aria-label="Skeins of pink, purple and cream yarn" style="background:linear-gradient(135deg,#6b63a8,#d58a8e 50%,#ece4d6)"></div><h4>LOREM IPSUM</h4><p>Lorem Ipsum is simply dummy text of the printing and typesetting industry.</p><div class="stars">★★★★★</div></div>
<div class="card" style="left:821px;top:2596px;width:254px;height:350px"><div class="img" role="img" aria-label="Stacks of colourful folded woven blankets" style="background:linear-gradient(135deg,#2c3f7a,#8a3a5a 40%,#2f7a6a 70%,#3a3a6a)"></div><h4>LOREM IPSUM</h4><p>Lorem Ipsum is simply dummy text of the printing and typesetting industry.</p><div class="stars">★★★★★</div></div>
<div class="card" style="left:546px;top:2946px;width:254px;height:350px"><div class="img" role="img" aria-label="Stack of soft white towels" style="background:linear-gradient(180deg,#d8d4cc,#efece6 50%,#cfcac0)"></div><h4>LOREM IPSUM</h4><p>Lorem Ipsum is simply dummy text of the printing and typesetting industry.</p><div class="stars">★★★★★</div></div>
<div class="card" style="left:821px;top:2979px;width:254px;height:348px"><div class="img" role="img" aria-label="Red woven rug with geometric pattern" style="background:linear-gradient(135deg,#b8401f,#d8704a 50%,#a8381c)"></div><h4>LOREM IPSUM</h4><p>Lorem Ipsum is simply dummy text of the printing and typesetting industry.</p><div class="stars">★★★★★</div></div>

<!-- Animals -->
<section class="abs animals">
  <div class="eyebrow">OUR ANIMALS</div>
  <h2>MEET OUR BELOVED FARM FAMILY</h2>
  <div class="acard" style="left:125px"><div class="img" role="img" aria-label="Black horse galloping in a paddock" style="background:linear-gradient(180deg,#9ab0c8,#a89a80 60%,#8a7a60)"></div><h4>LOREM IPSUM<small>(Male)</small></h4><p>Lorem Ipsum is simply dummy text of the printing and typesetting industry.</p><div class="stars">★★★★★</div><div class="price">$500.00</div></div>
  <div class="acard" style="left:367px"><div class="img" role="img" aria-label="Dark bay horse standing on a field" style="background:linear-gradient(180deg,#9fb3c4,#5a4030 55%,#7a8a4a)"></div><h4>LOREM IPSUM<small>(Female)</small></h4><p>Lorem Ipsum is simply dummy text of the printing and typesetting industry.</p><div class="stars">★★★★★</div><div class="price">$500.00</div></div>
  <div class="acard" style="left:610px"><div class="img" role="img" aria-label="Bay horse standing in a riding arena" style="background:linear-gradient(180deg,#6a8a5a,#7a4a2a 55%,#c8c0b0)"></div><h4>LOREM IPSUM<small>(Male)</small></h4><p>Lorem Ipsum is simply dummy text of the printing and typesetting industry.</p><div class="stars">★★★★★</div><div class="price">$500.00</div></div>
  <div class="acard" style="left:852px"><div class="img" role="img" aria-label="Bay horse standing in a riding arena" style="background:linear-gradient(180deg,#6a8a5a,#7a4a2a 55%,#c8c0b0)"></div><h4>LOREM IPSUM<small>(Female)</small></h4><p>Lorem Ipsum is simply dummy text of the printing and typesetting industry.</p><div class="stars">★★★★★</div><div class="price">$500.00</div></div>
  <div class="chev" style="left:110px;top:384px"><svg width="12" height="12" viewBox="0 0 12 12" fill="none" stroke="#0c2340" stroke-width="2"><path d="M8 2L4 6l4 4"/></svg></div>
  <div class="chev" style="left:1060px;top:384px"><svg width="12" height="12" viewBox="0 0 12 12" fill="none" stroke="#0c2340" stroke-width="2"><path d="M4 2l4 4-4 4"/></svg></div>
  <div class="btn light" style="left:526px;top:631px">VIEW ALL</div>
</section>

<!-- Testimonial / gallery -->
<div class="photo" style="left:0;top:4177px;width:600px;height:333px;background:linear-gradient(135deg,#2a2420,#4a3c30 50%,#221d1a)" role="img" aria-label="Horse inside a dark barn"></div>
<p class="abs" style="left:100px;top:4290px;width:400px;text-align:center;color:#fff">Lorem Ipsum is simply dummy text of the printing and typesetting industry. Lorem Ipsum has been the industry's standard dummy text ever since the 1500s, when an unknown printer took a galley of type and scrambled it to make a type specimen book.</p>
<div class="photo" style="left:600px;top:4177px;width:600px;height:333px;background:linear-gradient(180deg,#a8c4e0,#cfd8de 35%,#7a9a4a 60%,#6a8a3a)" role="img" aria-label="Pony grazing beside a white fence on a farm lane"></div>
<div class="chev white" style="left:35px;top:4328px"><svg width="12" height="12" viewBox="0 0 12 12" fill="none" stroke="#0c2340" stroke-width="2"><path d="M8 2L4 6l4 4"/></svg></div>
<div class="chev white" style="left:1135px;top:4328px"><svg width="12" height="12" viewBox="0 0 12 12" fill="none" stroke="#0c2340" stroke-width="2"><path d="M4 2l4 4-4 4"/></svg></div>

<!-- Footer -->
<footer class="abs footer">
  <div class="f-brand"><span class="dot"></span>LUNARA ALPACAS</div>
  <div class="socials"><span></span><span></span><span></span><span></span></div>
  <ul class="links">
    <h5>QUICK LINKS</h5>
    <li>Home</li><li>About Us</li><li>Animals</li><li>Shop</li><li>Inquire Now</li>
  </ul>
</footer>
<div class="tile-panel"></div>
<div class="tile" style="left:554px;top:4456px;background:linear-gradient(180deg,#9aa0a4,#7a6a50)" role="img" aria-label="Horses grazing near a farmhouse"></div>
<div class="tile" style="left:731px;top:4456px;background:linear-gradient(180deg,#4a4a3a,#8a6a4a)" role="img" aria-label="Group of alpacas close together"></div>
<div class="tile" style="left:904px;top:4456px;background:linear-gradient(180deg,#3a5a2a,#6a4a2a)" role="img" aria-label="Horses behind a wooden fence"></div>
<div class="tile" style="left:554px;top:4654px;background:linear-gradient(180deg,#8a9a6a,#c8c4b0)" role="img" aria-label="White alpaca walking in a paddock"></div>
<div class="tile" style="left:731px;top:4654px;background:linear-gradient(180deg,#6a8a4a,#5a6a3a)" role="img" aria-label="Horses in a green meadow"></div>
<div class="tile" style="left:904px;top:4654px;background:linear-gradient(180deg,#5a6a4a,#2a2a24)" role="img" aria-label="Black and white alpacas in a field"></div>
<div class="copy">© Copyright 2023&nbsp;<b>LUNARA ALPACAS</b>&nbsp;All rights reserved</div>

</body>
</html>
```